Upstart Retirement Planning Firm needs help with business card design

Harborline Wealth Partners, LLC is looking for help with business card design. We give advice on investments, insurance, and other financial matters related to retirement. There are some required disclosures that we will provide but mostly we are looking for a professional, classy business card that reflects the theme we have chosen. We have a logo that is attached but we would like to add a phrase; "Turning Your Earned Income Into Retirement Income"

Doubled sided only so that we can add the required disclosures (needed for our industry) on the back of the card. We will provide the exact words for this in 1-2 days.

Target Market(s)

Retirees and Pre-retirees. Professionals 50+ years old

Industry/Entity Type

Financial Planning

Contact Information for Business Card

We currently have two people who will need separate cards so we'd like to have a template so that we can add names for new cards in the future.

For the first run, please show the following information.

Grant Feloway, MBA, ChFC®, CLU®
Financial Advisor, Registered Representative
gfeloway@harborlinewp-example.com
Phone: (555) 218-3096
Toll Free Fax: (800) 555-3096

Address is
2187 Bramblecrest Ave.
Suite K418
Virginia Beach, VA 23999

Colors
3277b5

Requirements
Must have
• Logo, contact info, small phase to describe business (in description), required legal disclosures on back of the card as follows (in small font)
• Grant Feloway is a registered representative of and offers securities through Maplestead Capital Brokerage Corporation, Member NQBA. Maplestead Capital Brokerage Corporation is a member of the Maplestead Capital Group which is the marketing name for Maplestead Holdings Corporation and its affiliates.
Nice to have
• Rounded edges, raised letters
Should not have
• any colors that aren't in the logo (other than black for font)

```html
<!DOCTYPE html>
<html lang="en">
<head>
<meta charset="utf-8">
<title>Harborline Wealth Partners – Business Card</title>
<link rel="stylesheet" href="https://fonts.googleapis.com/css2?family=Arimo:wght@400;700&display=swap">
<style>
  :root {
    --stage: #1d1d1f;
    --paper: #f3f3f2;
    --brand-blue: #1f5aa6;
    --brand-blue-deep: #164a8f;
    --brand-grey: #9b9b9d;
    --ink: #222222;
    --rule: #cfcfcf;
    --white: #ffffff;
  }
  * { box-sizing: border-box; margin: 0; padding: 0; }
  html, body {
    width: 1200px; height: 1001px; overflow: hidden;
    background: var(--stage);
    font-family: "Arimo", Arial, sans-serif;
  }
  .canvas { position: relative; width: 1200px; height: 1001px; }

  .card {
    position: absolute;
    width: 589px; height: 330px;
    overflow: hidden;
  }

  /* Front */
  .card--front { left: 203px; top: 133px; background: var(--paper); }
  .brand-block {
    position: absolute; left: 30px; top: 80px; width: 290px;
    text-align: center;
  }
  .brand-name {
    font-size: 25px; font-weight: 400; line-height: 1.2;
    color: var(--brand-blue);
  }
  .tagline {
    margin-top: 38px;
    font-size: 14px; line-height: 18px; color: var(--ink);
  }
  .divider {
    position: absolute; left: 330px; top: 59px;
    width: 1px; height: 184px; background: var(--rule);
  }
  .details { position: absolute; left: 352px; top: 54px; color: var(--ink); }
  .person-name {
    font-size: 17.5px; font-weight: 700; color: var(--brand-blue);
    letter-spacing: 0.2px; line-height: 20px;
  }
  .credentials { font-size: 14px; line-height: 17.5px; }
  .contact-list { list-style: none; margin-top: 16px; }
  .contact-list li {
    display: flex; align-items: center; gap: 6px;
    font-size: 14px; line-height: 17.5px; white-space: nowrap;
  }
  .contact-list li.email { font-size: 11.8px; }
  .contact-icon { width: 14px; height: 14px; flex: none; }
  .address { margin-top: 16px; font-size: 14px; line-height: 17.5px; font-style: normal; }
  .band { position: absolute; bottom: 0; height: 17px; }
  .band--blue { left: 0; width: 334px; background: var(--brand-blue); }
  .band--grey { left: 341px; right: 0; background: var(--brand-grey); }

  /* Back */
  .card--back {
    left: 408px; top: 539px;
    background: linear-gradient(180deg, var(--brand-blue) 0%, var(--brand-blue-deep) 100%);
    color: var(--white); text-align: center;
  }
  .card--back .brand-name {
    position: absolute; left: 0; right: 0; top: 120px;
    color: var(--white); font-size: 28px;
  }
  .website {
    position: absolute; left: 0; right: 0; top: 270px;
    font-size: 13.5px; color: #dfe6f0;
  }
</style>
</head>
<body>
<main class="canvas">

  <section class="card card--front" aria-label="Card front">
    <div class="brand-block">
      <p class="brand-name">Harborline Wealth<br>Partners, LLC</p>
      <p class="tagline">Turning Your Earned Income<br>Into Retirement Income</p>
    </div>

    <div class="divider"></div>

    <div class="details">
      <h1 class="person-name">GRANT FELOWAY</h1>
      <p class="credentials">MBA, ChFC®, CLU®<br>Financial Advisor<br>Registered Representative</p>

      <ul class="contact-list">
        <li>
          <svg class="contact-icon" viewBox="0 0 14 14" aria-hidden="true">
            <rect width="14" height="14" rx="2" fill="#1f5aa6"/>
            <path d="M4.2 3c.5 0 1.3 1.6 1.3 2 0 .5-.8.7-.7 1.1.3.9 1.2 1.8 2.1 2.1.4.1.6-.7 1.1-.7.4 0 2 .8 2 1.3 0 .8-.9 1.6-1.7 1.6C5.6 10.4 3.6 8.4 3 5.2 2.6 4 3.4 3 4.2 3z" fill="#fff"/>
          </svg>
          (555) 218-3096
        </li>
        <li>
          <svg class="contact-icon" viewBox="0 0 14 14" aria-hidden="true">
            <rect width="14" height="14" rx="2" fill="#1f5aa6"/>
            <rect x="4.5" y="2.5" width="5" height="3" fill="none" stroke="#fff" stroke-width="1"/>
            <rect x="3" y="5.5" width="8" height="4" rx="0.6" fill="none" stroke="#fff" stroke-width="1"/>
            <rect x="4.5" y="8.5" width="5" height="3" fill="#1f5aa6" stroke="#fff" stroke-width="1"/>
          </svg>
          (800) 555-3096
        </li>
        <li class="email">
          <svg class="contact-icon" viewBox="0 0 14 14" aria-hidden="true">
            <rect width="14" height="14" rx="2" fill="#1f5aa6"/>
            <rect x="2.8" y="4" width="8.4" height="6" fill="none" stroke="#fff" stroke-width="1"/>
            <path d="M2.8 4 7 7.4 11.2 4" fill="none" stroke="#fff" stroke-width="1"/>
          </svg>
          gfeloway@harborlinewp-example.com
        </li>
      </ul>

      <address class="address">2187 Bramblecrest Ave.<br>Suite K418, Virginia Beach<br>VA 23999</address>
    </div>

    <div class="band band--blue"></div>
    <div class="band band--grey"></div>
  </section>

  <section class="card card--back" aria-label="Card back">
    <p class="brand-name">Harborline Wealth<br>Partners, LLC</p>
    <p class="website">www.harborlinewp-example.com</p>
  </section>

</main>
</body>
</html>
```